FLX & Harwick Solutions Business Card Design

a specialised consulting company, aviation specialist, like to have use blue colour on white background.
back of card to have printed-
NDT Expertise:
INSPECTION & TESTING CONSULTING
TRAINING & EDUCATION
CERTIFICATION SERVICES
LEVEL 3 SERVICES
VORTEM / AUDITING
INSPECTION SYSTEMS

Target Market(s)

Mainly the aerospace industry, manufacturers and airframe/engine overhaul companies.

Industry/Entity Type

Business

Contact Information for Business Card

FLX & Harwick Solutions

Derek Lomaxe JP

+61 (0)491570147
flxharwicksolutions@mailbox-demo.net

Font styles to use
Serif

Colors
3276b4
32a5d5

Requirements
Must have
• aviation style logo with letters FHS part of or adjacent to.

then company name: FLX & Harwick Solutions

then name in slightly smaller font : Derek Lomaxe JP

then phone and email details

Back of card, as per brief, but all text to be centred

```html
<!DOCTYPE html>
<html lang="en">
<head>
<meta charset="utf-8">
<title>FLX &amp; Harwick Solutions – Business Card</title>
<link rel="stylesheet" href="https://fonts.googleapis.com/css2?family=Roboto+Slab:wght@400;500;700&display=swap">
<style>
  :root {
    --backdrop: #d9d9d6;
    --card-white: #ffffff;
    --band-grey: #eef0f1;
    --brand-blue: #32a5d5;
    --brand-deep: #3276b4;
    --sky-light: #7fd0f2;
    --leaf-green: #8dbb35;
    --name-green: #5f9a2a;
    --ink: #2e3338;
    --icon-dark: #34383c;
  }
  * { box-sizing: border-box; margin: 0; padding: 0; }
  html, body { width: 1200px; height: 790px; overflow: hidden; }
  body {
    background: var(--backdrop);
    font-family: "Roboto Slab", serif;
    position: relative;
  }
  .card {
    position: absolute;
    width: 560px;
    height: 320px;
    overflow: hidden;
    box-shadow: 0 10px 26px rgba(0,0,0,0.22);
  }
  .brand-dot {
    flex: 0 0 auto;
    border-radius: 50%;
    background: var(--brand-blue);
  }
  .brand-name {
    font-weight: 700;
    color: var(--brand-blue);
    white-space: nowrap;
  }

  /* Back of card */
  .card-back {
    left: 40px; top: 60px;
    background: var(--card-white);
    display: flex;
    flex-direction: column;
    align-items: center;
    justify-content: center;
    text-align: center;
  }
  .card-back .brand-dot { width: 56px; height: 56px; }
  .card-back .brand-name { font-size: 24px; margin-top: 10px; }
  .expertise { margin-top: 16px; }
  .expertise-title {
    font-size: 13px; font-weight: 700; color: var(--brand-deep);
    letter-spacing: 0.5px; margin-bottom: 5px;
  }
  .expertise-list { list-style: none; }
  .expertise-list li {
    font-size: 10.5px; line-height: 15px; color: var(--ink);
    letter-spacing: 0.8px;
  }

  /* Front of card */
  .card-front {
    left: 600px; top: 410px;
    background: linear-gradient(125deg, var(--brand-blue) 0%, var(--sky-light) 45%, var(--brand-blue) 100%);
  }
  .top-strip {
    position: absolute; left: 0; top: 0; width: 100%; height: 12px;
    background: var(--brand-blue);
  }
  .header-band {
    position: absolute; left: 0; top: 12px; width: 100%; height: 88px;
    background: linear-gradient(180deg, var(--card-white), var(--band-grey));
    display: flex; align-items: center; gap: 12px;
    padding-left: 26px;
  }
  .header-band .brand-dot { width: 46px; height: 46px; }
  .header-band .brand-name { font-size: 22px; }
  .header-rule {
    position: absolute; left: 0; top: 100px; width: 100%; height: 4px;
    background: var(--card-white);
  }
  .contact-list {
    position: absolute; left: 290px; top: 118px; right: 0;
    list-style: none;
    display: flex; flex-direction: column; gap: 8px;
  }
  .contact-item {
    display: flex; align-items: stretch;
    background: var(--card-white);
    min-height: 22px;
    font-size: 9.5px; color: var(--ink);
  }
  .contact-icon {
    flex: 0 0 22px;
    background: var(--icon-dark);
    display: flex; align-items: center; justify-content: center;
  }
  .contact-text {
    padding: 0 7px; display: flex; align-items: center; line-height: 1.25;
    white-space: nowrap;
  }
  .contact-item.address { min-height: 36px; }
  .identity {
    position: absolute; left: 0; top: 232px; width: 240px; height: 48px;
    background: linear-gradient(90deg, var(--card-white), var(--band-grey));
    border-left: 9px solid var(--leaf-green);
    padding: 8px 14px;
  }
  .person-name {
    font-size: 14px; font-weight: 500; color: var(--name-green);
    letter-spacing: 0.8px; white-space: nowrap;
  }
  .person-role {
    font-size: 10px; color: var(--ink);
    letter-spacing: 0.8px; text-transform: uppercase; margin-top: 2px;
  }
</style>
</head>
<body>

<section class="card card-back" aria-label="Business card back">
  <span class="brand-dot"></span>
  <div class="brand-name">FLX &amp; Harwick Solutions</div>
  <div class="expertise">
    <div class="expertise-title">NDT Expertise:</div>
    <ul class="expertise-list">
      <li>INSPECTION &amp; TESTING CONSULTING</li>
      <li>TRAINING &amp; EDUCATION</li>
      <li>CERTIFICATION SERVICES</li>
      <li>LEVEL 3 SERVICES</li>
      <li>VORTEM / AUDITING</li>
      <li>INSPECTION SYSTEMS</li>
    </ul>
  </div>
</section>

<section class="card card-front" aria-label="Business card front">
  <div class="top-strip"></div>
  <header class="header-band">
    <span class="brand-dot"></span>
    <div class="brand-name">FLX &amp; Harwick Solutions</div>
  </header>
  <div class="header-rule"></div>

  <ul class="contact-list">
    <li class="contact-item">
      <span class="contact-icon"><svg width="12" height="12" viewBox="0 0 12 12"><path d="M3 1 L5 3 L4 4.5 Q5.5 7 7.5 8 L9 7 L11 9 L9.5 11 Q4 10 1 3 Z" fill="var(--leaf-green)"/></svg></span>
      <span class="contact-text">+61 (0)491570147</span>
    </li>
    <li class="contact-item">
      <span class="contact-icon"><svg width="12" height="12" viewBox="0 0 12 12"><rect x="3.5" y="1" width="5" height="10" rx="1" fill="none" stroke="var(--leaf-green)" stroke-width="1.2"/></svg></span>
      <span class="contact-text">+61 (0)491570147</span>
    </li>
    <li class="contact-item">
      <span class="contact-icon"><svg width="12" height="12" viewBox="0 0 12 12"><rect x="1" y="3" width="10" height="7" fill="var(--leaf-green)"/><path d="M1 3 L6 7 L11 3" fill="none" stroke="var(--icon-dark)" stroke-width="1"/></svg></span>
      <span class="contact-text">flxharwicksolutions@mailbox-demo.net</span>
    </li>
    <li class="contact-item">
      <span class="contact-icon"><svg width="12" height="12" viewBox="0 0 12 12"><circle cx="6" cy="6" r="4.5" fill="var(--leaf-green)"/></svg></span>
      <span class="contact-text">www.fhs-demo.net</span>
    </li>
    <li class="contact-item address">
      <span class="contact-icon"><svg width="12" height="14" viewBox="0 0 12 14"><path d="M6 13 Q1 7 1 5 A5 5 0 0 1 11 5 Q11 7 6 13 Z" fill="var(--leaf-green)"/><circle cx="6" cy="5" r="1.8" fill="var(--icon-dark)"/></svg></span>
      <span class="contact-text">27 Level 4 Orrin Harbour<br>Road AU</span>
    </li>
  </ul>

  <div class="identity">
    <div class="person-name">Derek Lomaxe JP</div>
    <div class="person-role">Financial Advisor</div>
  </div>
</section>

</body>
</html>
```